New Business Card Design Project

Need a design that will create an impact / strong impression towards our clients for our business. We are in the lighting business and we do lighting retrofits for large commercial to industrial clientele.

Target Market(s)

Lighting Industry

Industry/Entity Type

Business

Other font styles liked:
• we would like to use the font on our logo, not sure what it is though..

Requirements
Must have
• Our logo.
Nice to have
• We are open to suggestions that have to do with lighting.

```html
<!DOCTYPE html>
<html lang="en">
<head>
<meta charset="utf-8">
<title>Lumora Business Card</title>
<link rel="stylesheet" href="https://fonts.googleapis.com/css2?family=Arimo:wght@400;700&display=swap">
<style>
  :root {
    --bg: #d4d4d4;
    --card-front: #1f4a29;
    --card-pattern: #224f2d;
    --card-back: #ffffff;
    --green: #168a45;
    --green-dark: #1c4526;
    --text: #2a2a2a;
    --white: #ffffff;
  }
  * { margin: 0; padding: 0; box-sizing: border-box; }
  html, body { width: 900px; height: 1200px; overflow: hidden; }
  body {
    background: var(--bg);
    font-family: "Arimo", Arial, sans-serif;
    position: relative;
    color: var(--text);
  }
  .card {
    position: absolute;
    left: 84px;
    width: 734px;
    border-radius: 22px;
    overflow: hidden;
    box-shadow: 0 4px 10px rgba(0,0,0,0.25);
  }
  .card-front { top: 137px; height: 431px; background: var(--card-front); }
  .card-back { top: 633px; height: 429px; background: var(--card-back); }

  .front-pattern {
    position: absolute; inset: 0;
    background: linear-gradient(180deg, var(--card-pattern), var(--card-front));
  }
  .front-brand {
    position: absolute; left: 0; right: 0; top: 168px;
    display: flex; justify-content: center; align-items: center; gap: 18px;
  }
  .front-brand .brand-name {
    font-size: 74px; font-weight: 700; letter-spacing: 4px;
    color: var(--white); line-height: 1;
  }
  .front-brand .brand-mark { width: 52px; height: 52px; background: var(--white); }

  .name-band {
    position: absolute; left: 0; top: 59px;
    width: 246px; height: 68px;
    background: var(--green);
    padding: 12px 0 0 40px;
    color: var(--white);
  }
  .name-band .person { font-size: 23px; font-weight: 700; line-height: 1.1; }
  .name-band .role { font-size: 16px; margin-top: 3px; }
  .band-accent {
    position: absolute; left: 250px; top: 59px;
    width: 11px; height: 68px; background: var(--green-dark);
  }

  .back-brand {
    position: absolute; right: 40px; top: 62px;
    display: flex; align-items: center; gap: 14px;
  }
  .back-brand .brand-name {
    font-size: 58px; font-weight: 700; letter-spacing: 3px;
    color: var(--green-dark); line-height: 1;
  }
  .back-brand .brand-mark { width: 40px; height: 40px; background: var(--green); }

  .address {
    position: absolute; left: 40px; top: 273px;
    font-size: 16px; line-height: 25px;
  }
  .divider {
    position: absolute; left: 40px; right: 37px; top: 331px;
    height: 2px; background: var(--green-dark);
  }
  .contact-list {
    position: absolute; top: 345px;
    list-style: none; font-size: 16px; line-height: 24px;
  }
  .contact-list li { display: flex; align-items: center; gap: 8px; }
  .contact-phones { left: 40px; }
  .contact-web { right: 37px; text-align: right; }
  .contact-web li { justify-content: flex-end; }
  .icon { width: 17px; height: 17px; flex: none; }
</style>
</head>
<body>

  <section class="card card-front">
    <div class="front-pattern" role="img" aria-label="Faint repeated brand pattern across the card"></div>
    <div class="front-brand">
      <span class="brand-name">LUMORA</span>
      <span class="brand-mark"></span>
    </div>
  </section>

  <section class="card card-back">
    <div class="name-band">
      <div class="person">Daniel Reyes</div>
      <div class="role">Managing Director</div>
    </div>
    <div class="band-accent"></div>

    <div class="back-brand">
      <span class="brand-name">LUMORA</span>
      <span class="brand-mark"></span>
    </div>

    <address class="address" style="font-style:normal">
      412 W. Halden Ave, Suite 820<br>
      P.O. Box 48261
    </address>

    <div class="divider"></div>

    <ul class="contact-list contact-phones">
      <li>
        <svg class="icon" viewBox="0 0 17 17"><rect x="0.5" y="0.5" width="16" height="16" rx="2" fill="var(--green)"/><path d="M4 6 Q8.5 2.5 13 6 L12 7.5 L10 7 L10 6 Q8.5 5.3 7 6 L7 7 L5 7.5 Z M5.5 9 H11.5 V13 H5.5 Z" fill="#fff"/></svg>
        27-400-515-118
      </li>
      <li>
        <svg class="icon" viewBox="0 0 17 17"><rect x="0.5" y="0.5" width="16" height="16" rx="2" fill="var(--green)"/><rect x="5" y="3" width="7" height="11" rx="1" fill="#fff"/><rect x="6" y="4.5" width="5" height="6" fill="var(--green)"/></svg>
        27-615-372-904
      </li>
    </ul>

    <ul class="contact-list contact-web">
      <li>
        hello@lumora.com
        <svg class="icon" viewBox="0 0 17 17"><rect x="0.5" y="0.5" width="16" height="16" rx="2" fill="var(--green)"/><rect x="3.5" y="5" width="10" height="7" fill="#fff"/><path d="M3.5 5 L8.5 9 L13.5 5" stroke="var(--green)" stroke-width="1" fill="none"/></svg>
      </li>
      <li>
        www.lumora.com
        <svg class="icon" viewBox="0 0 17 17"><rect x="0.5" y="0.5" width="16" height="16" rx="2" fill="var(--green)"/><circle cx="8.5" cy="8.5" r="5" fill="none" stroke="#fff" stroke-width="1.2"/><ellipse cx="8.5" cy="8.5" rx="2" ry="5" fill="none" stroke="#fff" stroke-width="1"/><path d="M3.5 8.5 H13.5" stroke="#fff" stroke-width="1"/></svg>
      </li>
    </ul>
  </section>

</body>
</html>
```